Modern Lawfirm Business Card Design

We're looking for a business card to incorporate the newly created logo we had made.

Ideally looking for a law firm business card demonstrating, modern, minimalist, strong/bold design.

I'm open to any design honestly, but nothing "flashy".

Target Market(s)

Immigration law, family immigration, humanitarian, general legal

Industry/Entity Type

Law Firm

Contact Information for Business Card

Please use dummy information, name, street address, city, state, phone number, email, website.

Font styles to use
Serif
Sans Serif

Requirements
Must have
• Please use dummy information, name, street address, city, state, phone number, email, website.

```html
<!DOCTYPE html>
<html lang="en">
<head>
<meta charset="utf-8">
<title>Marlowe Immigration Law – Business Cards</title>
<link href="https://fonts.googleapis.com/css2?family=Source+Sans+3:wght@400;600&display=swap" rel="stylesheet">
<style>
  :root {
    --brand-blue: #1b4a85;
    --ink: #1c1c1c;
    --card: #ffffff;
    --backdrop: #e9e6e3;
  }
  * { margin: 0; padding: 0; box-sizing: border-box; }
  html, body { width: 1200px; height: 900px; overflow: hidden; }
  body {
    background: var(--backdrop);
    font-family: "Source Sans 3", "Segoe UI", sans-serif;
    position: relative;
  }
  .card {
    position: absolute;
    background: var(--card);
    box-shadow: 0 2px 8px rgba(0,0,0,0.12);
    overflow: hidden;
  }
  .card--front { left: 238px; top: 60px; width: 555px; height: 345px; }
  .card--back  { left: 457px; top: 518px; width: 560px; height: 344px; }

  .contact { position: absolute; left: 34px; top: 36px; color: var(--ink); }
  .contact__name { color: var(--brand-blue); font-size: 21px; font-weight: 600; line-height: 26px; }
  .contact__title { font-size: 15.5px; line-height: 20px; }
  .contact__address { margin-top: 13px; font-size: 15.5px; line-height: 20px; }
  .contact__list { list-style: none; margin-top: 12px; font-size: 15.5px; line-height: 20px; }
  .contact__list li { display: flex; align-items: center; gap: 9px; }
  .contact__list svg { width: 12px; height: 12px; fill: var(--brand-blue); flex: none; }

  .band { position: absolute; background: var(--brand-blue); }
  .wordmark {
    position: absolute;
    background: var(--brand-blue);
    color: #fff;
    font-weight: 600;
    display: flex; align-items: center; justify-content: center;
    white-space: nowrap;
    letter-spacing: 0.5px;
  }
  .card--front .band--left { left: 0; top: 251px; width: 245px; height: 56px; }
  .card--front .wordmark { left: 252px; top: 251px; width: 268px; height: 56px; font-size: 20px; }

  .card--back .band--left  { left: 0; top: 112px; width: 81px; height: 108px; }
  .card--back .band--right { left: 482px; top: 112px; width: 78px; height: 108px; }
  .card--back .wordmark { left: 90px; top: 125px; width: 380px; height: 77px; font-size: 28px; }
</style>
</head>
<body>
  <section class="card card--front" aria-label="Business card front">
    <div class="contact">
      <p class="contact__name">Daniel Harper</p>
      <p class="contact__title">Managing Director</p>
      <p class="contact__address">4821 Harbor Street, Suite 9<br>Springfield, IL 62701.</p>
      <ul class="contact__list">
        <li><svg viewBox="0 0 24 24" aria-hidden="true"><path d="M6.6 10.8c1.4 2.8 3.8 5.1 6.6 6.6l2.2-2.2c.3-.3.7-.4 1-.2 1.1.4 2.3.6 3.6.6.6 0 1 .4 1 1V20c0 .6-.4 1-1 1C10.6 21 3 13.4 3 4c0-.6.4-1 1-1h3.5c.6 0 1 .4 1 1 0 1.3.2 2.5.6 3.6.1.3 0 .7-.2 1L6.6 10.8z"/></svg>044-987 654 321</li>
        <li><svg viewBox="0 0 24 24" aria-hidden="true"><path d="M2 5h20v14H2z"/><path d="M3 6.5l9 6 9-6" fill="none" stroke="#fff" stroke-width="1.8"/></svg>info@marlowelaw.com</li>
        <li><svg viewBox="0 0 24 24" aria-hidden="true"><path d="M10.6 13.4a1 1 0 0 0 1.4 0l5-5a3 3 0 0 0-4.2-4.2l-1.6 1.6 1.4 1.4 1.6-1.6a1 1 0 0 1 1.4 1.4l-5 5a1 1 0 0 0 0 1.4zM13.4 10.6a1 1 0 0 0-1.4 0l-5 5a3 3 0 0 0 4.2 4.2l1.6-1.6-1.4-1.4-1.6 1.6a1 1 0 0 1-1.4-1.4l5-5a1 1 0 0 0 0-1.4z"/></svg>www.marlowelaw.com</li>
      </ul>
    </div>
    <div class="band band--left"></div>
    <div class="wordmark">Marlowe Immigration Law</div>
  </section>

  <section class="card card--back" aria-label="Business card back">
    <div class="band band--left"></div>
    <div class="wordmark">Marlowe Immigration Law</div>
    <div class="band band--right"></div>
  </section>
</body>
</html>
```